One page Flyer for Magician

I'm after a one Page Flyer

A4 Size - One sided
I want the finished artwork in 2 Forms.
One with the URL and one without the URL.

I need to be able to either print out myself in a small run ( I have a Vexo Colour PrintMaster)
or send out as a PDF attachment
or use on Website

I have attached the copy that should be included. 2 Words New doc
The Order of the sentences / testimonials / client list / locations worked
is not set so can be changed or played with to create a strong final image

I have attached one image to be incorporated

As you can see from the copy (or a visit to my website)
I'm after something that is -

Classy , Sophisticated, Smart, perhaps a bit quirky.

You can add other design elements in if needed , but Nothing "Corny Magic" like - eg no Rabbits , Wands, puffs of smoke

I have no corporate colour or logo or branding that should be included so you have a fairly free reign

```html
<!DOCTYPE html>
<html lang="en">
<head>
<meta charset="utf-8">
<title>Marcus Vale – Mentalist Flyer</title>
<link rel="stylesheet" href="https://fonts.googleapis.com/css2?family=Poiret+One&family=Varela+Round&family=Passion+One:wght@700&display=swap">
<style>
  :root {
    --page-bg: #e9e9ee;
    --band: #4d52a3;
    --band-strip: rgba(77, 82, 163, 0.5);
    --band-soft: rgba(88, 94, 170, 0.9);
    --night: #05060d;
    --name-blue: #3a40a6;
    --white: #ffffff;
    --quote-blue: #a9b4f0;
    --circle: rgba(82, 88, 166, 0.9);
  }
  * { box-sizing: border-box; margin: 0; padding: 0; }
  html, body { width: 927px; height: 1200px; overflow: hidden; }
  body { background: var(--page-bg); position: relative; font-family: "Varela Round", sans-serif; }

  .flyer {
    position: absolute; left: 22px; top: 30px; width: 813px; height: 1135px;
    background: var(--night); overflow: hidden;
    box-shadow: 0 4px 14px rgba(0,0,0,0.35);
  }
  .headline-band {
    position: absolute; left: 0; top: 0; width: 100%; height: 120px;
    background: var(--band);
    display: flex; flex-direction: column; align-items: center; justify-content: center;
    color: var(--white); font-family: "Poiret One", sans-serif; font-weight: 400;
    font-size: 35px; line-height: 40px; text-transform: uppercase; letter-spacing: 1px;
    text-align: center; -webkit-text-stroke: 1.6px var(--white);
  }
  .headline-band::after {
    content: ""; position: absolute; left: 0; right: 0; bottom: -36px; height: 36px;
    background: var(--band-strip);
  }
  .performer-name {
    position: absolute; left: 0; width: 100%; top: 176px; text-align: center;
    font-family: "Passion One", sans-serif; font-weight: 700; font-size: 70px; line-height: 80px;
    color: var(--name-blue); -webkit-text-stroke: 2px var(--white);
    transform: skewX(-12deg); letter-spacing: 1px;
  }
  .tagline {
    position: absolute; left: 0; width: 100%; top: 258px; text-align: center;
    color: var(--white); font-size: 33px; line-height: 40px; font-style: italic;
    -webkit-text-stroke: 0.8px var(--white);
  }
  .credentials {
    position: absolute; left: 0; top: 320px; width: 100%; height: 232px;
    background: var(--band-soft); color: var(--white);
    padding: 8px 56px 0; text-align: center; font-size: 17.5px; line-height: 25px;
  }
  .credentials strong { font-weight: 700; -webkit-text-stroke: 0.5px var(--white); }
  .credentials em { font-style: italic; -webkit-text-stroke: 0.5px var(--white); }

  .performer-photo {
    position: absolute; left: 290px; top: 552px; width: 520px; height: 540px;
    background: radial-gradient(ellipse 55% 50% at 50% 45%, #343c8a 0%, #1a1f50 45%, rgba(5,6,13,0) 100%);
  }
  .testimonial {
    position: absolute; border-radius: 50%; background: var(--circle);
    display: flex; flex-direction: column; align-items: center; justify-content: center;
    text-align: center; color: var(--quote-blue); font-style: italic;
    font-size: 23px; line-height: 32px; -webkit-text-stroke: 0.4px var(--quote-blue);
  }
  .testimonial-left { left: 33px; top: 602px; width: 280px; height: 280px; }
  .testimonial-right { left: 522px; top: 720px; width: 258px; height: 258px; }

  .footer-wave { position: absolute; left: 0; bottom: 0; width: 813px; height: 160px; }
  .website {
    position: absolute; left: 0; width: 100%; bottom: 14px; text-align: center;
    color: var(--white); font-size: 21px; font-weight: 700; letter-spacing: 1px;
    -webkit-text-stroke: 0.6px var(--white);
  }
</style>
</head>
<body>
  <article class="flyer">
    <header class="headline-band">
      <span>Experience the sophisticated comedy and</span>
      <span>mind-reading of mentalist</span>
    </header>

    <h1 class="performer-name">MARCUS VALE</h1>
    <p class="tagline">“Australia’s Maestro of Minds”</p>

    <section class="credentials">
      <p>Booked and rebooked by the world’s leading Cruise Lines to provide sophisticated entertainment for their discerning audiences<br>
      <strong>Lumen, Harwick, Azurelle, Regent Star, Southern Tide Australia.</strong><br>
      Corporate &amp; Association clients also take him around the world for his astounding, interactive and easily staged show or to provide his unique MC services.<br>
      <em>Recent assignments - Hawaii, New Zealand, South Africa,<br>Hong Kong and all states of Australia.</em></p>
    </section>

    <div class="performer-photo" role="img" aria-label="Photo of the mentalist in a blue suit on stage at a microphone, against a starry night backdrop"></div>

    <blockquote class="testimonial testimonial-left">
      <span>“Outstanding!”</span>
      <span>CEO , Australian</span>
      <span>Council of Trade</span>
      <span>&amp; Enterprise</span>
    </blockquote>
    <blockquote class="testimonial testimonial-right">
      <span>“Brilliant!”</span>
      <span>CEO, Coral Clayworks</span>
    </blockquote>

    <svg class="footer-wave" viewBox="0 0 813 160" aria-hidden="true">
      <path d="M0 20 Q406 110 813 20 L813 160 L0 160 Z" fill="#4d52a3" opacity="0.55"/>
      <path d="M0 40 Q406 125 813 40 L813 160 L0 160 Z" fill="#4d52a3"/>
    </svg>
    <footer class="website">www.MindMarvelAustralia.com</footer>
  </article>
</body>
</html>
```